Outdoor group fitness training - Greta Pollock Personal Training

I want an eye catching A4 flyer that promotes my two outdoor fitness groups. I have uploaded photos of each location: Brenton and Kilvane.
The target group is existing and potential new Personal training clients - all adults. There are two morning groups at Brenton ; one evening and one morning group at Kilvane. The groups will be for up to 8 people and are for all fitness levels.I want to encourage people to come and have a go. I have also uploaded a design I have used through inkrally for a previous flyer. I would like to use the orange graphic of the two people at the bottom of this design.
Cost is $15 per person
Location and times - Brenton Green Wednesdays 7.30am; Sundays 8am
Kilvane High School Thursdays 6.30pm: Saturdays 8am
Updates

Thanks so much to all of you for submitting a great set of designs. it was really hard making a choice in the end, and I really appreciate the promptness and creativity that went into the designs. I will certainly keep you in mind for future jobs. Cheers and have a great day Greta Pollock

Target Market(s)

40 - 60 year old adults: cross section of professionals, tradespeople and retirees. People who will enjoy socialising while also getting fit. No extremely fit people - cross section of beginners to intermediate; males and females

Industry/Entity Type

Training

Font styles to use
Sans Serif

Colors
f78f20
9bcb3c
ecf7fb

Requirements
Must have
• Fast turnaround required - within two days
Bright and attention grabbing, engaging. Could be A4 or could be postcard size?

State cost clearly
State that first 5 people to join either group will get first session at half price

```html
<!DOCTYPE html>
<html lang="en">
<head>
<meta charset="utf-8">
<title>Greta Pollock Flyer – Postcard 4x6</title>
<link rel="stylesheet" href="https://fonts.googleapis.com/css2?family=Arimo:ital,wght@0,400;0,700;1,700&family=Open+Sans:wght@400;700&family=Russo+One&display=swap">
<style>
  :root {
    --orange: #f78f20;
    --green: #9bcb3c;
    --sky: #ecf7fb;
    --ink: #1d1d1d;
    --black: #000;
    --white: #fff;
    --rule: #8a8a8a;
    --park-green: #6f8a4e;
    --park-sky: #c9d8e4;
    --path-grey: #9b9588;
    --run-dusk: #8c7a68;
  }
  * { margin: 0; padding: 0; box-sizing: border-box; }
  html, body { width: 927px; height: 1200px; overflow: hidden; background: var(--white); }
  body { position: relative; font-family: "Arimo", Arial, sans-serif; color: var(--ink); }

  .sheet-title { position: absolute; left: 56px; top: 70px; font-size: 20px; }
  .side-label { position: absolute; left: 159px; font-size: 19px; }
  .side-label--a { top: 100px; }
  .side-label--b { top: 636px; }

  .card { position: absolute; left: 150px; width: 670px; border: 1.5px solid var(--black); overflow: hidden; }
  .card--front { top: 133px; height: 446px; background: var(--sky); }
  .card--back { top: 668px; height: 444px; background: var(--white); }

  /* front */
  .front__topbar { position: absolute; left: 0; top: 0; width: 100%; height: 17px; background: var(--orange); }
  .front__headline { position: absolute; left: -40px; width: 750px; top: 22px; text-align: center; white-space: nowrap;
    font-family: "Russo One", sans-serif; font-weight: 400; color: var(--green);
    font-size: 50px; line-height: 56px; letter-spacing: 2px;
    transform: skewX(-10deg) scaleX(0.82); transform-origin: center; }
  .front__trainer { position: absolute; left: 0; width: 100%; top: 82px; text-align: center; white-space: nowrap;
    font-weight: 700; font-style: italic; color: var(--orange); font-size: 25px; }
  .front__scene { position: absolute; left: 0; top: 112px; width: 670px; height: 280px; }
  .place-label { position: absolute; color: var(--white); font-size: 17px; }
  .place-label--kilvane { left: 15px; top: 312px; }
  .place-label--brenton { left: 355px; top: 291px; }
  .price-badge { position: absolute; left: 444px; top: 178px; width: 176px; height: 176px; border-radius: 50%;
    background: var(--black); color: var(--white); font-weight: 700; font-size: 34px; line-height: 1.15;
    display: flex; align-items: center; justify-content: center; text-align: center; }
  .front__dates { position: absolute; left: 12px; top: 380px; font-family: "Russo One", sans-serif;
    font-size: 20px; line-height: 1.1; color: var(--ink); text-transform: uppercase; white-space: nowrap;
    transform: skewX(-10deg); transform-origin: left top; }
  .front__offer { position: absolute; left: 0; bottom: 0; width: 100%; height: 16px; background: var(--black); white-space: nowrap;
    color: var(--white); font-weight: 700; font-size: 13px; letter-spacing: 1px; text-align: center; line-height: 16px; }

  /* back */
  .back__info { position: absolute; left: 0; top: 0; width: 352px; height: 225px; background: var(--green);
    color: var(--white); font-family: "Open Sans", sans-serif; font-size: 16.5px; line-height: 23px; padding: 12px 0 0 16px; }
  .back__info strong { font-weight: 700; }
  .back__info .gap { height: 23px; }
  .back__photo { position: absolute; left: 0; top: 225px; width: 352px; height: 198px;
    background: linear-gradient(180deg, #b6a48d 0%, var(--run-dusk) 55%, #5b4e43 100%); }
  .back__photo-strip { position: absolute; left: 0; top: 395px; width: 228px; height: 28px; background: var(--white); }
  .back__photo-notch { position: absolute; left: 0; top: 252px; width: 52px; height: 26px; background: var(--white); }
  .back__mark { position: absolute; left: 10px; top: 400px; width: 22px; height: 18px; background: var(--orange); border-radius: 3px; }
  .stamp-box { position: absolute; left: 561px; top: 9px; width: 92px; height: 103px; border: 1px solid var(--rule); }
  .address-line { position: absolute; left: 360px; width: 293px; height: 1px; background: var(--rule); }
  .welcome { position: absolute; left: 352px; width: 318px; top: 340px; text-align: center;
    font-weight: 700; color: var(--green); font-size: 21px; line-height: 31px; letter-spacing: 0.5px; }
  .back__contact { position: absolute; left: 0; bottom: 0; width: 100%; height: 21px; background: var(--orange); white-space: nowrap;
    color: var(--white); font-size: 16px; line-height: 21px; padding-left: 38px; }
</style>
</head>
<body>
  <div class="sheet-title">Greta Pollock Flyer-- Postcard 4x6 | First Draft</div>

  <div class="side-label side-label--a">Side A:</div>
  <section class="card card--front">
    <div class="front__topbar"></div>
    <svg class="front__scene" viewBox="0 0 670 280" xmlns="http://www.w3.org/2000/svg">
      <defs>
        <clipPath id="scene-band">
          <path d="M0 30 C120 5 220 55 340 35 C460 15 560 5 670 30 L670 210 C560 240 440 215 330 235 C210 255 110 265 0 240 Z"/>
        </clipPath>
        <linearGradient id="kilvane-park" x1="0" y1="0" x2="0" y2="1">
          <stop offset="0" stop-color="var(--park-sky)"/>
          <stop offset="0.45" stop-color="var(--park-green)"/>
          <stop offset="1" stop-color="var(--path-grey)"/>
        </linearGradient>
        <linearGradient id="brenton-park" x1="0" y1="0" x2="0" y2="1">
          <stop offset="0" stop-color="#a9c0cf"/>
          <stop offset="0.5" stop-color="#587a45"/>
          <stop offset="1" stop-color="#7e9a5a"/>
        </linearGradient>
      </defs>
      <g clip-path="url(#scene-band)">
        <rect x="0" y="0" width="315" height="280" fill="url(#kilvane-park)" role="img" aria-label="Photo of the Kilvane park training ground with trees and a path"/>
        <rect x="315" y="0" width="355" height="280" fill="url(#brenton-park)" role="img" aria-label="Photo of Brenton Green oval with a shelter and gum trees"/>
      </g>
      <path d="M0 30 C120 5 220 55 340 35 C460 15 560 5 670 30 L670 14 C560 -8 460 2 340 22 C220 42 120 -8 0 18 Z" fill="var(--green)"/>
      <path d="M0 240 C110 265 210 255 330 235 C440 215 560 240 670 210 L670 226 C560 258 440 232 330 250 C210 270 110 280 0 256 Z" fill="var(--green)"/>
    </svg>
    <h1 class="front__headline">OUTDOOR FITNESS GROUP</h1>
    <p class="front__trainer">Greta Pollock, Master Trainer Certificate IV in Fitness</p>
    <span class="place-label place-label--kilvane">Kilvane</span>
    <span class="place-label place-label--brenton">Brenton</span>
    <div class="price-badge">$15 per<br>person</div>

    <p class="front__dates">Groups running from<br>November 12th to February 23rd</p>
    <div class="front__offer">FIRST 5 PEOPLE TO JOIN EITHER GROUP WILL GET FIRST SESSION AT HALF PRICE</div>
  </section>

  <div class="side-label side-label--b">Side B:</div>
  <section class="card card--back">
    <div class="back__info">
      <div>LOCATION &amp; TIMES:</div>
      <div><strong>Kilvane High School,</strong></div>
      <div>Hollis Road, Kilvane, CA</div>
      <div>Thurs. 6:30PM &amp; Sat. 8AM</div>
      <div class="gap"></div>
      <div>Brenton Green</div>
      <div>214 - 216 Carrow Road</div>
      <div>Brenton, CA</div>
      <div>Wed. 7:30AM &amp; Sun. 8AM</div>
    </div>
    <div class="back__photo" role="img" aria-label="Photo of two people running along a waterfront path at dusk"></div>
    <div class="back__photo-notch"></div>
    <div class="back__photo-strip"></div>
    <div class="back__mark" role="img" aria-label="Small orange graphic of two runners"></div>

    <div class="stamp-box"></div>
    <div class="address-line" style="top:182px"></div>
    <div class="address-line" style="top:228px"></div>
    <div class="address-line" style="top:275px"></div>
    <div class="address-line" style="top:321px"></div>

    <p class="welcome">ALL FITNESS<br>LEVELS WELCOME!</p>
    <div class="back__contact">Contact Greta for more information: 0400 555 217 gpollock@mailhaven.com</div>
  </section>
</body>
</html>
```